Velorant Flyer

PROJECT: Digital Flyer for VeloRant

Format
1920 × 1080 px (landscape, optimized for presentations and email)
Deliverables
• PDF
• PNG

About VeloRant
VeloRant is a Dutch B2B software company providing a unified CRM and customer journey platform. We help businesses manage the entire customer lifecycle — from first contact to loyal customer — by centralizing all touchpoints in one system.
What sets us apart:
Extreme ease of use. The system is self-guiding, shows only what's relevant per employee, and requires virtually no training. All channels (email, phone, chat, in-store) come together in one place with automatic task distribution. Built-in AI functions as a smart digital colleague that continuously learns.
Target audience:
Directors and sales managers at B2B companies with multiple customer contact channels.

Goal:
We want to create a flyer that sets us apart from other CRM platform providers. Our aim is to achieve this through simplicity and a professional appearance. The design should reflect our core value: ease of use. The recipient should feel compelled to engage with us — not overwhelmed by information, but intrigued by clarity. Less is more.

Required Text Elements
Headline:
"CRM that adapts to how you work"
Subline:
"Discover how VeloRant simplifies your sales process"
Call-to-action:
"See it in action — book a call"
Contact details:
• hello@velorant.nl
• 023-5871469
• velorant.com

Required Visual Elements
• VeloRant logo (attached)

Design Style
• Modern / Minimalist
• Professional / Business
• Tech / Futuristic
• Clean with plenty of whitespace

Tone of voice:
Clear, positive and customer-focused. Practical and accessible business style aimed at communicating concrete value for users.

Design inspiration — please review these websites:
• orbitfen.com
• tavolo.app
• quillet.com
• norvadex.com
• plumbit.com
What We DON'T Want
• Bold / In-your-face
• Dense / Compact
• Trendy / Experimental
• Childlike / Cheerful
• Playful / Cartoonish
• Busy / Chaotic
Colors
Use the color palette from velorant.com (blues, whites, clean professional tones).
[Exact hex codes used for element on the website:
#344054;
#1a1b1f;
#0254ac
#002249;
#e5edf7;
background-color: #fff; ]
Competitors (for context only — do NOT copy)
• vendhaven.nl
• kelpnode.com
• marrowcrm.com
• tradewinder.com
Budget
$150
Deadline
January 26, 2026

```html
<!DOCTYPE html>
<html lang="en">
<head>
<meta charset="utf-8">
<title>VeloRant Flyer</title>
<link href="https://fonts.googleapis.com/css2?family=Figtree:wght@400;500;700;800&display=swap" rel="stylesheet">
<style>
  :root {
    --navy: #002249;
    --blue: #0254ac;
    --tick: #1e9ad6;
    --text: #344054;
    --ink: #1a1b1f;
    --pale: #e5edf7;
    --white: #ffffff;
    --rule: #d6d9de;
    --tag-bg: #dcf2cf;
    --tag-text: #2f6b1d;
  }
  * { margin: 0; padding: 0; box-sizing: border-box; }
  html, body { width: 1200px; height: 675px; overflow: hidden; background: var(--white); }
  body { font-family: "Figtree", sans-serif; color: var(--navy); position: relative; }

  .sky { position: absolute; left: 0; top: 0; }

  .brand-top {
    position: absolute; left: 52px; top: 68px;
    font-size: 44px; font-weight: 800; color: var(--navy); letter-spacing: -0.5px;
  }
  .headline {
    position: absolute; left: 48px; top: 186px;
    font-size: 52px; font-weight: 800; line-height: 53px; letter-spacing: -0.5px; color: var(--navy);
  }
  .subline {
    position: absolute; left: 50px; top: 318px;
    font-size: 24px; font-weight: 400; line-height: 28px; color: var(--navy);
  }
  .subline strong { font-weight: 700; }
  .cta {
    position: absolute; left: 50px; top: 417px; width: 312px; height: 61px;
    background: var(--blue); border-radius: 10px; color: var(--white);
    font-size: 21px; font-weight: 400; display: flex; align-items: center; justify-content: center;
    text-decoration: none;
  }

  .benefit {
    position: absolute; height: 41px; background: var(--navy); border-radius: 21px;
    color: var(--white); font-size: 22px; font-weight: 400;
    display: flex; align-items: center; gap: 18px; padding-left: 18px;
  }
  .benefit svg { width: 32px; height: 26px; flex: none; }
  .benefit-1 { left: 719px; top: 93px; width: 380px; }
  .benefit-2 { left: 681px; top: 145px; width: 353px; }
  .benefit-3 { left: 643px; top: 197px; width: 319px; gap: 44px; }

  .app-tile {
    position: absolute; left: 452px; top: 387px; width: 122px; height: 123px;
    background: var(--white); border-radius: 24px;
    box-shadow: 0 0 0 14px rgba(255,255,255,0.45), 0 8px 30px rgba(120,110,180,0.15);
  }

  .laptop {
    position: absolute; left: 645px; top: 282px; width: 475px; height: 272px;
    border-radius: 14px 14px 6px 6px;
    background: linear-gradient(180deg, #f4f6fa 0%, #e9edf3 70%, #9aa0a8 100%);
    box-shadow: 0 10px 24px rgba(0,0,0,0.12);
  }

  .contact-card {
    position: absolute; left: 862px; top: 366px; width: 242px; height: 72px;
    background: var(--white); border-radius: 12px;
    box-shadow: 0 6px 20px rgba(0,34,73,0.14);
    padding: 9px 0 0 30px;
  }
  .contact-card .card-icon {
    position: absolute; left: 8px; top: 10px; width: 18px; height: 18px;
    border-radius: 50%; background: var(--tag-bg);
  }
  .contact-card .card-name { font-size: 12.5px; font-weight: 500; color: var(--text); }
  .contact-card .card-meta { font-size: 10.5px; color: #667085; margin-top: 4px; }
  .contact-card .card-tags { display: flex; gap: 6px; margin-top: 6px; }
  .tag {
    font-size: 11px; background: var(--tag-bg); color: var(--tag-text);
    padding: 1px 8px; border-radius: 9px;
  }

  .cursor { position: absolute; left: 1048px; top: 418px; width: 56px; height: 80px; }

  .footer-rule {
    position: absolute; left: 50px; top: 589px; width: 1100px; height: 1px; background: var(--rule);
  }
  .footer-brand {
    position: absolute; left: 50px; top: 614px; font-size: 31px; font-weight: 800; color: var(--navy);
  }
  .contact {
    position: absolute; top: 618px; display: flex; align-items: center; gap: 5px;
    font-size: 25px; font-weight: 400; color: var(--navy);
  }
  .contact svg { width: 26px; height: 26px; flex: none; }
  .contact-email { left: 380px; }
  .contact-phone { left: 706px; }
  .contact-web { left: 960px; }
</style>
</head>
<body>

  <svg class="sky" width="1200" height="675" viewBox="0 0 1200 675" role="img" aria-label="Soft pastel sky with clouds in lilac, pink and peach tones">
    <defs>
      <linearGradient id="skyTone" x1="0" y1="0" x2="0.4" y2="1">
        <stop offset="0" stop-color="#d9d8f2"/>
        <stop offset="0.45" stop-color="#e8d6ea"/>
        <stop offset="1" stop-color="#f6dcd6"/>
      </linearGradient>
      <clipPath id="skyClip"><rect x="0" y="0" width="1200" height="589"/></clipPath>
    </defs>
    <circle cx="1072" cy="419" r="550" fill="url(#skyTone)" clip-path="url(#skyClip)"/>
  </svg>

  <div class="brand-top">VeloRant</div>

  <h1 class="headline">CRM that adapts to<br>how you work</h1>

  <p class="subline">Discover how <strong>VeloRant</strong> simplifies<br>your sales process</p>

  <a class="cta" href="#">See it in action / Book a call</a>

  <div class="benefit benefit-1">
    <svg viewBox="0 0 32 26"><path d="M3 14 L12 22 L29 4" fill="none" stroke="var(--tick)" stroke-width="6"/></svg>
    One unified customer journey
  </div>
  <div class="benefit benefit-2">
    <svg viewBox="0 0 32 26"><path d="M3 14 L12 22 L29 4" fill="none" stroke="var(--tick)" stroke-width="6"/></svg>
    AI-powered daily assistance
  </div>
  <div class="benefit benefit-3">
    <svg viewBox="0 0 32 26"><path d="M3 14 L12 22 L29 4" fill="none" stroke="var(--tick)" stroke-width="6"/></svg>
    Zero-training CRM
  </div>

  <div class="app-tile"></div>

  <div class="laptop" role="img" aria-label="Laptop showing the CRM contact board with columns of customer cards"></div>

  <div class="contact-card">
    <span class="card-icon"></span>
    <div class="card-name">Mara Holt, Lumen Works</div>
    <div class="card-meta">Last activity 13 Sep 2025</div>
    <div class="card-tags"><span class="tag">Done</span><span class="tag">Relation</span></div>
  </div>

  <svg class="cursor" viewBox="0 0 56 80">
    <path d="M6 4 L50 50 L32 52 L44 74 L34 78 L22 56 L8 68 Z" fill="var(--tick)" stroke="var(--white)" stroke-width="3" stroke-linejoin="round"/>
  </svg>

  <div class="footer-rule"></div>

  <div class="footer-brand">VeloRant</div>

  <div class="contact contact-email">
    <svg viewBox="0 0 26 26"><rect x="1.5" y="5" width="23" height="16" fill="none" stroke="var(--navy)" stroke-width="1.6"/><path d="M1.5 5 L13 15 L24.5 5" fill="none" stroke="var(--navy)" stroke-width="1.6"/></svg>
    hello@velorant.nl
  </div>
  <div class="contact contact-phone">
    <svg viewBox="0 0 26 26"><path d="M6 3 L10 3 L12 9 L9 11 Q12 17 15 19 L17 16 L23 18 L23 22 Q22 24 19 24 Q5 20 2 6 Q3 3 6 3 Z" fill="none" stroke="var(--navy)" stroke-width="1.6" stroke-linejoin="round"/></svg>
    023-5871469
  </div>
  <div class="contact contact-web">
    <svg viewBox="0 0 26 26" fill="none" stroke="var(--navy)" stroke-width="1.6"><circle cx="13" cy="13" r="11"/><ellipse cx="13" cy="13" rx="5" ry="11"/><path d="M2 13 H24 M4 7 H22 M4 19 H22"/></svg>
    velorant.com
  </div>

</body>
</html>
```